New Chartered Accounting Practice Needs Stationery Design

I need a new set of stationery including letterhead, business cards, envelopes and with compliments slips for a new Chartered Accounting Practice based in Melbourne, Victoria, Australia called "Martin K. Ashbury, Chartered Accountant".
I will be providing Taxation Services, Accounting Services, Self-Managed Superannuation Fund Consulting and general consulting advice to small and medium business enterprises. I would like to see designs that use the colour blue. The final design should communicate trust, technical expertise and security.
Target Market(s)
English speaking, Australians. Proprietors of small and medium businesses - aged 30-65. Fellow professionals - lawyers, investment consultants, other accountants. Retirees - aged 60 and over
Industry/Entity Type
Business
Look and feel

```html
<!DOCTYPE html>
<html lang="en">
<head>
<meta charset="utf-8">
<title>Martin K. Ashbury – Envelope</title>
<link rel="stylesheet" href="https://fonts.googleapis.com/css2?family=Carlito:wght@400;700&display=swap">
<style>
  :root {
    --paper: #ffffff;
    --band-top: #8aafd9;
    --band-bottom: #1158a7;
    --brand-blue: #1c5aa8;
    --ink: #1a1a1a;
    --rule: #7fa6d6;
    --window-line: #3a3a3a;
  }
  * { margin: 0; padding: 0; box-sizing: border-box; }
  html, body {
    width: 1200px; height: 510px; overflow: hidden;
    background: var(--paper);
    font-family: "Carlito", "Calibri", sans-serif;
  }
  .envelope {
    position: relative; width: 1200px; height: 510px;
    background: var(--paper); overflow: hidden;
  }
  .top-band {
    position: absolute; left: 0; top: 0; width: 100%; height: 26px;
    background: var(--band-top);
  }
  .bottom-band {
    position: absolute; left: 0; bottom: 0; width: 100%; height: 42px;
    background: var(--band-bottom);
  }
  .flap-tab {
    position: absolute; left: 902px; top: 458px; width: 170px; height: 26px;
    background: var(--paper);
    border-radius: 0 0 24px 24px;
  }
  .brand {
    position: absolute; left: 74px; top: 58px;
    display: flex; align-items: center; gap: 22px;
  }
  .brand-square {
    width: 78px; height: 78px; background: var(--brand-blue);
  }
  .brand-text { color: var(--brand-blue); font-weight: 400; }
  .brand-name {
    font-size: 34px; letter-spacing: 1px; line-height: 1.1;
    text-transform: uppercase;
  }
  .brand-rule {
    height: 1px; width: 240px; background: var(--rule); margin: 6px 0 4px 22px;
  }
  .brand-title { font-size: 27px; line-height: 1.1; margin-left: 22px; }
  .divider {
    position: absolute; left: 518px; top: 58px; width: 1.5px; height: 102px;
    background: var(--rule);
  }
  .contact {
    position: absolute; left: 536px; top: 56px;
    list-style: none; color: var(--ink); font-size: 16px; line-height: 1.15;
  }
  .contact li { display: flex; align-items: flex-start; gap: 10px; margin-bottom: 4px; }
  .contact .icon { width: 22px; height: 22px; flex: none; fill: var(--ink); }
  .contact .lines { display: flex; flex-direction: column; padding-top: 1px; }
  .address-window {
    position: absolute; left: 98px; top: 314px; width: 612px; height: 143px;
    border: 1.2px solid var(--window-line); border-radius: 26px;
  }
</style>
</head>
<body>
<div class="envelope">
  <div class="top-band"></div>

  <div class="brand">
    <div class="brand-square"></div>
    <div class="brand-text">
      <div class="brand-name">Martin K. Ashbury</div>
      <div class="brand-rule"></div>
      <div class="brand-title">Chartered Accountant</div>
    </div>
  </div>

  <div class="divider"></div>

  <ul class="contact">
    <li>
      <svg class="icon" viewBox="0 0 24 24" aria-hidden="true"><path d="M12 2a7 7 0 0 0-7 7c0 5 7 13 7 13s7-8 7-13a7 7 0 0 0-7-7zm0 9.5A2.5 2.5 0 1 1 12 6.5a2.5 2.5 0 0 1 0 5z"/></svg>
      <span class="lines"><span>Address Line 1</span><span>Address Line 2</span></span>
    </li>
    <li>
      <svg class="icon" viewBox="0 0 24 24" aria-hidden="true"><path d="M3 9c0-3 4-5 9-5s9 2 9 5v1h-5V8.5c-1-.5-2.5-.7-4-.7s-3 .2-4 .7V10H3V9zm3 2h12l2 9H4l2-9zm6 2a3 3 0 1 0 0 6 3 3 0 0 0 0-6z"/></svg>
      <span class="lines"><span>+61 3 9000 4120, +61 3 9000 4121</span></span>
    </li>
    <li>
      <svg class="icon" viewBox="0 0 24 24" aria-hidden="true"><path d="M2 5h20v14H2V5zm2 2v.5l8 5 8-5V7H4z"/></svg>
      <span class="lines"><span>Email@website.com</span></span>
    </li>
    <li>
      <svg class="icon" viewBox="0 0 24 24" aria-hidden="true" fill="none" stroke="#1a1a1a" stroke-width="1.6"><circle cx="12" cy="12" r="9"/><ellipse cx="12" cy="12" rx="4" ry="9"/><path d="M3 12h18M5 7h14M5 17h14"/></svg>
      <span class="lines"><span>www.website.com</span></span>
    </li>
  </ul>

  <div class="address-window"></div>

  <div class="bottom-band"></div>
  <div class="flap-tab"></div>
</div>
</body>
</html>
```